Business school needs a web design

Who We are:
TUNAVE is a small business school that offers programs in Project Management. The school is based in West Africa and welcomes students from the whole area. Our aim is to become one of the reference business schools in Africa.

Project Brief:
The site will include all informations relevant for different types of visitors that we have: actual and future students, companies, mass media, future employees, ect. It will present information about subscription, list of programs, presentation of the school and its team,etc.

What We want:
This competition is for Design only no coding! We need design for two pages.
We did some wireframing for the home page and the list of programs page. We made them just to show how we imagine the website would look like. But we encourage creative designs, so you don't have to stick to the wireframe models.

Sites We like:
http://www.larchmontgate.example/
http://www.pelvarin.example/fr/etudes.html
http://www.qwd.example/mba/Pages/default.aspx

Color schemes
The logo of the school is red and black. So the color scheme of the website should match that. For the rest, it is opened to your imagination.
Updates

The payment for the project is now garanteed. Good luck to you all !

Target Market(s)

The target market is diversified because we have students of different ages, also company representatives or employees that might visit the website for recruitment purposes. But the majority of our audience should be aged between 20 - 30 years.

Industry/Entity Type

Small Business

Requirements
Must have
• The design must include two pages: a home page and another interior page : might be the list of programs or any other page relevant to the domain. The Home page must include a slide show at the beginning.
The background page must be white.
Nice to have
• The use of flat design for this project is preferred.
The use of Twitter bootstrap as a base for the design is an asset.

```html
<!DOCTYPE html>
<html lang="fr">
<head>
<meta charset="utf-8">
<title>TUNAVE — École de gestion</title>
<link rel="stylesheet" href="https://fonts.googleapis.com/css2?family=Jost:wght@300;400;500;600&family=Open+Sans:wght@400;600&family=Arimo:wght@400;700&display=swap">
<style>
:root{
  --red:#b30000;
  --red-dark:#8e0000;
  --red-text:#d61414;
  --ink:#333;
  --muted:#666;
  --line:#dcdcdc;
  --page:#f8f8f8;
  --link:#2a63b8;
}
*{box-sizing:border-box;margin:0;padding:0}
html,body{width:1200px;height:900px;overflow:hidden}
body{background:var(--page);font-family:"Open Sans",sans-serif;color:var(--ink);position:relative}
.topbar{position:absolute;top:0;left:0;width:1200px;height:4px;background:#111}
.site-header{position:absolute;top:4px;left:0;width:1200px;height:124px;background:#fff}
.brand{position:absolute;left:40px;top:38px;display:flex;align-items:center;gap:10px;font-family:"Jost",sans-serif;font-weight:600;font-size:30px;color:var(--red);letter-spacing:1px}
.brand-mark{width:18px;height:18px;background:var(--red)}
.utility{position:absolute;right:352px;top:31px;font-family:"Open Sans",sans-serif;font-size:12px;color:#666;display:flex;gap:6px}
.utility .active{color:var(--red)}
.utility .sep{color:#333;font-weight:600}
.search{position:absolute;left:875px;top:25px;width:267px;height:31px;border:1px solid #ccc;background:#fff;font-size:13px;color:#555;padding:6px 13px}
.search svg{position:absolute;right:9px;top:6px}
.main-nav{position:absolute;left:324px;top:68px;width:818px;height:42px;background:linear-gradient(#c60a0a,#a60000);border-radius:4px;display:flex;box-shadow:0 2px 3px rgba(0,0,0,.2)}
.main-nav a{font-family:"Arimo",sans-serif;font-weight:700;font-size:13px;color:#fff;text-decoration:none;display:flex;align-items:center;justify-content:center;border-right:1px solid #8b0000;box-shadow:1px 0 0 #d23a3a}
.main-nav a:last-child{border:none;box-shadow:none}
.hero{position:absolute;top:128px;left:0;width:1200px;height:412px;overflow:hidden}
.hero-photo{position:absolute;inset:0;background:linear-gradient(90deg,#4b5d5f 0%,#647677 35%,#8d9c9e 55%,#5a5f63 75%,#c8ccce 100%)}
.hero-photo::after{content:"";position:absolute;left:0;right:0;bottom:0;height:110px;background:linear-gradient(transparent,#1d1f21)}
.hero-copy{position:absolute;left:42px;top:84px;color:#fff}
.hero-kicker{font-family:"Jost",sans-serif;font-weight:600;font-size:29px;letter-spacing:.5px}
.hero-title{font-family:"Jost",sans-serif;font-weight:300;font-size:57px;line-height:1.1;margin-top:2px}
.hero-text{font-size:14.5px;line-height:24px;color:#e4e4e4;width:410px;margin-top:12px;margin-left:2px}
.btn-outline{position:absolute;left:3px;top:191px;width:170px;height:46px;border:1px solid #ddd;color:#fff;font-family:"Arimo",sans-serif;font-weight:700;font-size:14px;display:flex;align-items:center;justify-content:center}
.slider-tab{position:absolute;left:532px;top:516px;width:110px;height:28px;background:var(--red);border-radius:10px 10px 0 0;display:flex;gap:5px;justify-content:center;padding-top:8px}
.slider-tab span{width:10px;height:10px;border-radius:50%;background:#fff}
.slider-tab span.on{background:#111}
.hero-rule{position:absolute;top:538px;left:0;width:1200px;height:6px;background:var(--red);border-bottom:2px solid var(--red-dark)}
.audience{position:absolute;left:40px;top:600px;width:218px;height:286px;background:#fff;border:1px solid #ddd;border-radius:3px;padding:18px 20px}
.audience h3{font-family:"Arimo",sans-serif;font-weight:400;color:var(--red-text);font-size:19px;margin-bottom:13px}
.audience li{list-style:none;font-family:"Arimo",sans-serif;font-size:13px;color:#444;height:32px;line-height:32px;border-bottom:1px solid #e4e4e4}
.audience li:last-child{border:none}
.intro{position:absolute;left:285px;top:610px;width:597px}
.intro h2{font-family:"Jost",sans-serif;font-weight:500;font-size:20px;letter-spacing:.3px;color:#3a3a3a}
.intro p{font-size:13px;line-height:20px;color:#555;margin-top:9px}
.btn-red{display:inline-block;margin-top:14px;width:119px;height:37px;background:var(--red);border-radius:3px;color:#fff;font-family:"Arimo",sans-serif;font-weight:700;font-size:14px;text-align:center;line-height:37px}
.divider{position:absolute;left:285px;top:764px;width:597px;height:3px;border-top:1px solid #ddd;border-bottom:1px solid #ddd}
.blog-title{position:absolute;left:285px;top:785px;font-family:"Jost",sans-serif;font-weight:500;font-size:19px;color:#3a3a3a}
.blog-card{position:absolute;top:825px;width:186px;height:90px;background:#fff;border:1px solid #ddd;padding:4px}
.blog-card div{width:100%;height:100%}
.news{position:absolute;left:904px;top:601px;width:247px;height:310px;background:#fff;border:1px solid #ddd;border-radius:3px}
.news-head{height:42px;background:var(--red);border-radius:3px 3px 0 0;display:flex;justify-content:space-between;align-items:center;padding:0 16px 0 19px;color:#fff}
.news-head h3{font-family:"Jost",sans-serif;font-weight:500;font-size:18px}
.news-head span{font-family:"Arimo",sans-serif;font-size:12px}
.news-item{position:absolute;left:18px;width:211px;height:79px;border-bottom:1px solid #ddd}
.news-thumb{position:absolute;left:0;top:0;width:56px;height:56px;border:1px solid #ccc;padding:2px;background:#fff}
.news-thumb div{width:100%;height:100%;background:linear-gradient(135deg,#d92a2a,#e65a4a 50%,#9c8e86)}
.news-item h4{position:absolute;left:72px;top:0;font-weight:400;font-size:13.5px;color:var(--link)}
.news-item p{position:absolute;left:72px;top:22px;font-family:"Arimo",sans-serif;font-size:12.5px;line-height:14px;color:#555;width:130px}
</style>
</head>
<body>
<div class="topbar"></div>
<header class="site-header">
  <div class="brand"><span class="brand-mark"></span>TUNAVE</div>
  <nav class="utility">
    <span class="active">Repertoire du personel</span><span class="sep">I</span>
    <span>Blogue</span><span class="sep">I</span>
    <span>Solle de presse</span><span class="sep">I</span>
    <span>Nous joindre</span><span class="sep">I</span>
    <span>Francois</span>
  </nav>
  <div class="search">Search
    <svg width="18" height="18" viewBox="0 0 18 18"><circle cx="7" cy="7" r="5" fill="none" stroke="#888" stroke-width="2.4"/><line x1="11" y1="11" x2="16" y2="16" stroke="#888" stroke-width="3" stroke-linecap="round"/></svg>
  </div>
  <nav class="main-nav">
    <a style="width:177px">A propos de l'TUNAVE</a>
    <a style="width:214px">Programmes et Formations</a>
    <a style="width:102px">Etudiants</a>
    <a style="width:200px">Nouvelles et Evenements</a>
    <a style="width:125px">Entreprises</a>
  </nav>
</header>

<section class="hero">
  <div class="hero-photo" role="img" aria-label="Photo: a man in a suit leaning over an office desk with a computer, city view through the window"></div>
  <div class="hero-copy">
    <div class="hero-kicker">An innovative graduate</div>
    <div class="hero-title">School of theology</div>
    <p class="hero-text">Lorem Ipsum is simply dummy text of the printing and type-setting industry. Lorem Ipsum has been</p>
    <div class="btn-outline">MORE INFO</div>
  </div>
</section>
<div class="hero-rule"></div>
<div class="slider-tab"><span></span><span></span><span></span><span class="on"></span></div>

<aside class="audience">
  <h3>Vous etes</h3>
  <ul>
    <li>Futur Etudiont</li><li>Eludiont octuel</li><li>Entreprise</li><li>Employeur</li><li>Postulant</li><li>Madias</li><li>Partenaires</li>
  </ul>
</aside>

<section class="intro">
  <h2>TUNAVE : DEVENEZ LES GESTIONNAIRES DE DEMAIN</h2>
  <p>Cr66e pour former des professlonnels de haut niveau capobles de plan/tier et de rGollser des projets et programmes en respectant les contralntes de coOts, d6lol$, quality....</p>
  <span class="btn-red">MORE INFO</span>
</section>
<div class="divider"></div>
<h3 class="blog-title">blogue</h3>
<div class="blog-card" style="left:285px"><div role="img" aria-label="Photo: smiling student outdoors" style="background:linear-gradient(#a9c98a,#d6b48f)"></div></div>
<div class="blog-card" style="left:489px"><div role="img" aria-label="Photo: student on campus" style="background:linear-gradient(#5f7a4c,#b48d70)"></div></div>
<div class="blog-card" style="left:695px"><div role="img" aria-label="Photo: graduate in cap and gown" style="background:linear-gradient(#e6e6e6,#8a7a6a)"></div></div>

<aside class="news">
  <div class="news-head"><h3>Nouvelles</h3><span>View all</span></div>
  <div class="news-item" style="top:63px"><div class="news-thumb"><div role="img" aria-label="News photo"></div></div><h4>New Students Orient</h4><p>Lorem ipsum dolor is sit omet,</p></div>
  <div class="news-item" style="top:142px"><div class="news-thumb"><div role="img" aria-label="News photo"></div></div><h4>New Students Orient</h4><p>Lorem ipsum dolor is sit omet,</p></div>
  <div class="news-item" style="top:220px"><div class="news-thumb"><div role="img" aria-label="News photo"></div></div><h4>New Students Orient</h4><p>Lorem ipsum dolor is sit omet,</p></div>
</aside>
</body>
</html>
```